BrambleWare business card

Looking for business card design that supports our company/software values. We have 2 logo designs at the moment but open to change if you think you can enhance the brand. Check out website www.brambleware.com.au.

Target Market(s)

Education

Contact Information for Business Card

Name, title, mobile, email and website

Font styles to use
Sans Serif

Colors

Designer to choose colors to be used in the design.

Requirements
Must have
• BrambleWare logo with tree and tagline on rear side with dark grey background colour

```html
<!DOCTYPE html>
<html lang="en">
<head>
<meta charset="utf-8">
<title>BrambleWare business card</title>
<link rel="stylesheet" href="https://fonts.googleapis.com/css2?family=Lato:wght@400;700;900&display=swap">
<style>
  :root {
    --stage: #ecebe8;
    --charcoal: #4d4d4d;
    --white: #ffffff;
    --green: #4ccb0a;
    --ink: #333333;
  }
  * { margin: 0; padding: 0; box-sizing: border-box; }
  html, body { width: 1200px; height: 900px; overflow: hidden; }
  body {
    background: var(--stage);
    font-family: "Lato", Arial, sans-serif;
    position: relative;
  }
  .card {
    position: absolute;
    top: 296px;
    width: 540px;
    height: 309px;
    border-radius: 3px;
    overflow: hidden;
    box-shadow: 0 6px 18px rgba(0,0,0,0.18);
  }
  .card--back { left: 40px; background: var(--charcoal); }
  .card--front { left: 620px; background: var(--white); }

  .brand { position: absolute; display: flex; align-items: center; gap: 10px; }
  .brand__dot { border-radius: 50%; background: var(--green); flex: none; }
  .brand__name { font-weight: 400; letter-spacing: 0.5px; line-height: 1; }

  .card--back .brand { left: 50%; top: 50%; transform: translate(-50%, -50%); }
  .card--back .brand__dot { width: 30px; height: 30px; }
  .card--back .brand__name { font-size: 40px; color: var(--white); }

  .card--front .brand { right: 30px; top: 62px; }
  .card--front .brand__dot { width: 22px; height: 22px; }
  .card--front .brand__name { font-size: 30px; color: var(--charcoal); }

  .person { position: absolute; left: 44px; top: 64px; }
  .person__name { color: var(--green); font-weight: 900; font-size: 22px; letter-spacing: 0.5px; }
  .person__title { color: var(--ink); font-size: 14px; margin-top: 2px; }

  .contact { position: absolute; left: 44px; top: 160px; list-style: none; color: var(--ink); font-size: 16px; }
  .contact li { display: flex; align-items: center; gap: 8px; line-height: 21px; }
  .contact svg { width: 13px; height: 13px; flex: none; }
  .contact__address { margin-top: 8px; display: block !important; line-height: 20px; }

  .wave { position: absolute; inset: 0; width: 100%; height: 100%; }
</style>
</head>
<body>
  <section class="card card--back" aria-label="Card back">
    <div class="brand">
      <span class="brand__dot"></span>
      <span class="brand__name">BrambleWare</span>
    </div>
  </section>

  <section class="card card--front" aria-label="Card front">
    <svg class="wave" viewBox="0 0 540 309" preserveAspectRatio="none" aria-hidden="true">
      <path d="M540,148 C440,160 360,250 250,290 C200,305 150,309 110,309 L540,309 Z" fill="var(--charcoal)"/>
      <path d="M0,282 C140,292 300,268 430,205 C330,272 190,300 90,309 L0,309 Z" fill="var(--green)"/>
    </svg>

    <div class="person">
      <div class="person__name">DANIEL HARTLEY</div>
      <div class="person__title">Managing Director</div>
    </div>

    <div class="brand">
      <span class="brand__dot"></span>
      <span class="brand__name">BrambleWare</span>
    </div>

    <ul class="contact">
      <li>
        <svg viewBox="0 0 16 16"><path fill="var(--green)" d="M3 1l3 3-2 2c1 2 3 4 5 5l2-2 3 3-2 3C7 15 1 9 0 4z"/></svg>
        046-218 390 517
      </li>
      <li>
        <svg viewBox="0 0 16 16"><rect x="0" y="3" width="16" height="11" rx="1" fill="var(--green)"/><path d="M1 4l7 5 7-5" fill="none" stroke="#fff" stroke-width="1.4"/></svg>
        hello@brambleware.com
      </li>
      <li>
        <svg viewBox="0 0 16 16"><circle cx="8" cy="8" r="7.5" fill="var(--green)"/><circle cx="8" cy="8" r="3" fill="#fff"/></svg>
        www.brambleware.com.au
      </li>
      <li class="contact__address">37, Fernhill Road<br>30218, Southland</li>
    </ul>
  </section>
</body>
</html>
```